Stationary and business cards for TerraQuestia-an Education, Enrichment, and Conservation Ctr
TerraQuestia (top line) Education, Enrichment, Conservation
Stationary and business cards for TerraQuestia-an Education, Enrichment, and Conservation Ctr - Animals
Creative Brief
Bright & Fun-filled
Tova Ruth Kellerby-Doane
Executive Director
483 Brindwick Rd. suite 300 Ostervale, MD 20947
tovark@mailcove.example
www.TerraQuestia.example
I would like it to have foliage or vines coming out of the sides like rainforest...maybe a red eye tree frog somewhere and a morpho butterfly... Want it to be simple but classy....and want to be able to have the names and contact info to be interchangeable for all my employees. For the stationary I want the logo somewhere as well. Thank you!
The logo
tovark tovark
I like the leaf addition, but instead of putting it in the back...can you replace the lines in the front of the business card and putting the leaf outlines? That goes better with our theme than "professional" looking lines etc.... thanks!
I can't find how to attach the logo?
quintonhalvard7314065 quintonhalvard7314065
i need the logo logo are not attach in Brief
you can go to our website to get an idea of who we are www.TerraQuestia.example and see our logo.

```html
<!DOCTYPE html>
<html lang="en">
<head>
<meta charset="utf-8">
<title>TerraQuestia Business Card</title>
<link rel="stylesheet" href="https://fonts.googleapis.com/css2?family=Oswald:wght@300;400;600&display=swap">
<style>
  :root {
    --bg-light: #f1f1f1;
    --bg-dark: #d9d9d9;
    --card: #ffffff;
    --brown: #6a4810;
    --green: #3f9f2a;
    --ink: #3a3a3a;
    --ink-soft: #5e5e5e;
    --on-band: #ffffff;
  }
  * { box-sizing: border-box; margin: 0; padding: 0; }
  html, body { width: 1200px; height: 883px; overflow: hidden; }
  body {
    position: relative;
    background: radial-gradient(ellipse at 55% 35%, var(--bg-light), var(--bg-dark));
    font-family: "Oswald", "Arial Narrow", sans-serif;
    color: var(--ink);
  }
  .card {
    position: absolute;
    width: 520px;
    height: 297px;
    background: var(--card);
    border-radius: 22px;
    overflow: hidden;
    box-shadow: 0 10px 28px rgba(0,0,0,0.18);
  }

  /* Back side */
  .card-back { left: 580px; top: 120px; }
  .brand {
    position: absolute;
    left: 30px; top: 70px;
    width: 240px; height: 100px;
    display: flex; flex-direction: column; justify-content: center; align-items: center;
    gap: 6px;
  }
  .brand-row { display: flex; align-items: center; gap: 10px; }
  .brand-dot { width: 14px; height: 14px; border-radius: 50%; background: var(--green); }
  .brand-name { font-size: 32px; font-weight: 600; color: var(--brown); letter-spacing: 0.5px; }
  .brand-tagline { font-size: 10px; font-weight: 400; color: var(--green); letter-spacing: 0.8px; }
  .back-band {
    position: absolute;
    left: 300px; right: 0; top: 92px; height: 44px;
    background: var(--brown);
    display: flex; align-items: center; padding-left: 16px;
  }
  .back-band::after {
    content: ""; position: absolute; right: 0; top: 0; bottom: 0; width: 42px; background: var(--green);
  }
  .back-web { font-size: 11px; color: var(--on-band); letter-spacing: 0.4px; }

  /* Front side */
  .card-front { left: 120px; top: 450px; }
  .person { position: absolute; top: 32px; left: 0; right: 0; text-align: center; }
  .person-name { font-size: 26px; letter-spacing: 0.8px; color: var(--ink); line-height: 1.2; }
  .person-name .given { font-weight: 300; }
  .person-name .family { font-weight: 600; }
  .person-title { font-size: 11px; font-weight: 600; letter-spacing: 0.8px; color: var(--ink-soft); margin-top: 2px; }
  .front-band {
    position: absolute;
    left: 0; right: 0; top: 104px; height: 104px;
    background: var(--brown);
    color: var(--on-band);
  }
  .front-band::before {
    content: ""; position: absolute; left: 0; top: 46px; bottom: 0; width: 14px; background: var(--green);
  }
  .contact { position: absolute; font-size: 14px; line-height: 1.3; letter-spacing: 0.5px; }
  .contact-phone { left: 44px; top: 44px; }
  .contact-web { right: 40px; top: 18px; text-align: right; }
  .contact-label { font-weight: 400; }
  .address {
    position: absolute; top: 222px; left: 0; right: 0; text-align: center;
    font-size: 11px; letter-spacing: 0.5px; color: var(--ink); line-height: 1.45;
  }
  .address .locality { font-weight: 600; }
</style>
</head>
<body>
  <section class="card card-back" aria-label="Business card back">
    <div class="brand">
      <div class="brand-row">
        <span class="brand-dot"></span>
        <span class="brand-name">TerraQuestia</span>
      </div>
      <span class="brand-tagline">Education · Enrichment · Conservation</span>
    </div>
    <div class="back-band">
      <span class="back-web">www.TerraQuestia.example</span>
    </div>
  </section>

  <section class="card card-front" aria-label="Business card front">
    <div class="person">
      <p class="person-name"><span class="given">TOVA RUTH </span><span class="family">KELLERBY-DOANE</span></p>
      <p class="person-title">EXECUTIVE DIRECTOR</p>
    </div>
    <div class="front-band">
      <div class="contact contact-phone">
        <p class="contact-label">PHONE &amp; FAX</p>
        <p>+1 410 555 0142</p>
        <p>+1 410 555 0187</p>
      </div>
      <div class="contact contact-web">
        <p class="contact-label">EMAIL &amp; WEB</p>
        <p>TOVARK@MAILCOVE.EXAMPLE</p>
        <p>WWW.TERRAQUESTIA.EXAMPLE</p>
      </div>
    </div>
    <div class="address">
      <p>483 BRINDWICK RD. SUITE 300</p>
      <p class="locality">OSTERVALE, MD 20947</p>
    </div>
  </section>
</body>
</html>
```